Tarvel Ridge LLC

Need Professional Business cards for New Investment Fund

Target Market(s)

High Quality investors

Industry/Entity Type

Financial

Contact Information for Business Card

Phone Number +1 555 284 6193
Name Pavel Orlinsky
Title Fund Manager
email po@FundTarvel.example
Website www.FundTarvel.example

Colors

Designer to choose colors to be used in the design.

Requirements
Must have
• Must have our Logo and all of the above. Must be made so lettering and loge can be raised

```html
<!DOCTYPE html>
<html lang="en">
<head>
<meta charset="utf-8">
<title>Tarvel Ridge LLC – Business Card</title>
<link href="https://fonts.googleapis.com/css2?family=Open+Sans:wght@400;600;700&display=swap" rel="stylesheet">
<style>
  :root {
    --page: #ffffff;
    --card: #232323;
    --green: #46c13a;
    --muted: #3a3a3a;
    --faint: #2c2c2c;
    --edge: #3fb534;
  }
  * { box-sizing: border-box; margin: 0; padding: 0; }
  html, body { width: 1200px; height: 900px; overflow: hidden; background: var(--page); }
  body { position: relative; font-family: "Open Sans", Arial, sans-serif; }

  .card {
    position: absolute;
    left: 320px;
    width: 560px;
    height: 320px;
    background: var(--card);
    border: 3px solid var(--edge);
    border-radius: 2px;
    overflow: hidden;
  }
  .card--front { top: 80px; }
  .card--back { top: 480px; }

  /* Front */
  .holder-name {
    position: absolute; left: 40px; top: 52px;
    color: var(--green); font-weight: 700; font-size: 20px;
  }
  .divider {
    position: absolute; left: 40px; top: 86px;
    width: 440px; height: 3px; background: var(--green);
  }
  .holder-title {
    position: absolute; left: 40px; top: 96px;
    color: var(--green); font-size: 12px; opacity: .85;
  }
  .contact-row {
    position: absolute; left: 40px;
    display: flex; align-items: center; gap: 10px;
    color: var(--green); font-size: 13px;
  }
  .contact-row svg { width: 16px; height: 16px; flex: none; }
  .contact-row--phone { top: 140px; }
  .contact-row--email { top: 168px; }
  .contact-row--web { top: 260px; left: 200px; }

  .company-name {
    position: absolute; right: 75px; top: 54px;
    font-size: 18px; font-weight: 700; white-space: nowrap;
  }
  .company-name .lead { color: var(--green); }
  .company-name .tail { color: var(--muted); font-weight: 600; }

  .brand-mark {
    position: absolute; right: 26px; top: 150px;
    display: flex; align-items: center; gap: 8px;
    color: var(--green); font-size: 15px; font-weight: 700;
  }
  .brand-mark .dot { width: 12px; height: 12px; background: var(--green); }

  /* Back */
  .brand-mark--large {
    position: absolute; left: 40px; top: 40px;
    display: flex; align-items: center; gap: 16px;
    color: var(--faint); font-size: 48px; font-weight: 700;
  }
  .brand-mark--large .dot { width: 36px; height: 36px; background: var(--faint); }
  .card--back .company-name { right: 30px; top: auto; bottom: 28px; font-size: 22px; }
</style>
</head>
<body>

<section class="card card--front" aria-label="Business card front">
  <div class="company-name"><span class="lead">Tarvel Ridge</span> <span class="tail">LLC</span></div>
  <div class="holder-name">Pavel Orlinsky</div>
  <div class="divider"></div>
  <div class="holder-title">Fund Manager</div>

  <div class="contact-row contact-row--phone">
    <svg viewBox="0 0 16 16" aria-hidden="true"><rect x="1" y="1" width="14" height="14" rx="2" fill="var(--green)"/><path d="M5.5 4c.6 0 1 1.6 1 2s-.8.6-.6 1.2c.4 1 1.1 1.7 2 2 .5.2.7-.6 1.1-.6s2 .4 2 1-1 1.6-2 1.4C6.5 10.5 4.5 8.5 4 6c-.2-1 .9-2 1.5-2z" fill="var(--card)"/></svg>
    <span>+1 555 284 6193</span>
  </div>
  <div class="contact-row contact-row--email">
    <svg viewBox="0 0 16 16" aria-hidden="true"><rect x="1" y="3" width="14" height="10" fill="var(--green)"/><path d="M1 3l7 6 7-6" fill="none" stroke="var(--card)" stroke-width="1.3"/></svg>
    <span>po@FundTarvel.example</span>
  </div>
  <div class="contact-row contact-row--web">
    <svg viewBox="0 0 16 16" aria-hidden="true" fill="none" stroke="var(--green)" stroke-width="1.2"><circle cx="8" cy="8" r="6.5"/><ellipse cx="8" cy="8" rx="3" ry="6.5"/><path d="M1.5 8h13M2.5 4.7h11M2.5 11.3h11"/></svg>
    <span>www.FundTarvel.example</span>
  </div>

  <div class="brand-mark"><span class="dot"></span><span>Tarvel Ridge</span></div>
</section>

<section class="card card--back" aria-label="Business card back">
  <div class="brand-mark--large"><span class="dot"></span><span>Tarvel Ridge</span></div>
  <div class="company-name"><span class="lead">Tarvel Ridge</span> <span class="tail">LLC</span></div>
</section>

</body>
</html>
```